Meridale Cleaning Services

In need of a business card design suited for a growing cleaning company.

We offer our cleaning and maintenance services to a wide range of clients including but not limited to the following: constuction industry, hospitality, commercial, industrial and domestic

I want the card to be very noticable, i would like people to say 'hey, great card!' when i hand them my card.double sided would be nice

we want our business to come across as exceedingly professional and innovative (different).

a contemporary design is what we have in mind
we want to present an image of a quality business with a high standard of excellence in consistent service.

i just really need a card that persuades top end quality,
our business is very certified and also strives towards environmentaly friendly alternatives
Updates

hey sorry, i have uploaded my company logo design and name
cheers.

hey guys i have added my company logo/name file on my brief page. many thanks

sorry guys a typo in the brief..
address is Tolley Rd. not Tolly Rd
thanks

Industry/Entity Type

Industrial

Requirements
Must have
• company name: meridale cleaning services
operations manager: Colm Varetti
Tel: (02)9373 6204
Fax: (02)8645 7712
Mob: 0438571490

address: 47 Tolly RD Pymble NSW 2073
Postal Adress: PO Box 5832 North Ryde NSW 2113
email: meridaleclean@wexanet.com.au
website: meridalecleaningservices.com.au

```html
<!DOCTYPE html>
<html lang="en">
<head>
<meta charset="utf-8">
<title>Meridale Cleaning Services – Business Card</title>
<link rel="stylesheet" href="https://fonts.googleapis.com/css2?family=Source+Sans+3:wght@300;400;600;700&display=swap">
<style>
  :root {
    --brand-blue: #1b72ba;
    --logo-blue: #1f6fb6;
    --ink: #231f20;
    --muted: #7a7a7a;
    --contact: #2a2a2a;
    --paper: #ffffff;
    --on-blue: #ffffff;
    --on-blue-soft: #e3eef8;
  }
  html, body {
    margin: 0;
    padding: 0;
    width: 981px;
    height: 1200px;
    overflow: hidden;
    background: var(--paper);
  }
  .card {
    position: relative;
    width: 981px;
    height: 1200px;
    font-family: "Source Sans 3", "Myriad Pro", Arial, sans-serif;
    color: var(--ink);
    overflow: hidden;
  }
  .card-front {
    position: absolute;
    inset: 0 0 auto 0;
    height: 600px;
    background: var(--paper);
  }
  .card-back {
    position: absolute;
    inset: 600px 0 0 0;
    background: var(--brand-blue);
    color: var(--on-blue);
  }

  /* Brand mark */
  .brand {
    position: absolute;
    left: 283px;
    top: 70px;
    display: flex;
    align-items: center;
    gap: 20px;
  }
  .brand-dot {
    width: 116px;
    height: 116px;
    border-radius: 50%;
    background: var(--logo-blue);
    flex: none;
  }
  .brand-name {
    color: var(--logo-blue);
    font-weight: 700;
    line-height: 1;
  }
  .brand-name .primary {
    display: block;
    font-size: 66px;
    letter-spacing: -0.5px;
  }
  .brand-name .secondary {
    display: block;
    font-size: 25px;
    letter-spacing: 0.5px;
    margin-top: 6px;
  }

  /* Person */
  .person {
    position: absolute;
    left: 0;
    right: 0;
    top: 258px;
    text-align: center;
  }
  .person-name {
    margin: 0;
    font-size: 33px;
    font-weight: 600;
    color: var(--ink);
    line-height: 1.2;
  }
  .person-role {
    margin: 10px 0 0;
    font-size: 23px;
    font-weight: 400;
    color: var(--muted);
  }

  /* Contact numbers */
  .contact-list {
    position: absolute;
    left: 382px;
    top: 408px;
    margin: 0;
    display: grid;
    grid-template-columns: 42px auto;
    row-gap: 4px;
    font-size: 29px;
    line-height: 32px;
    color: var(--contact);
  }
  .contact-list dt {
    color: var(--muted);
    font-weight: 400;
  }
  .contact-list dd {
    margin: 0;
    font-weight: 400;
  }
  .email {
    position: absolute;
    left: 0;
    right: 0;
    top: 528px;
    text-align: center;
    font-size: 26px;
    color: var(--muted);
  }

  /* Back panel */
  .company {
    position: absolute;
    left: 233px;
    top: 90px;
    line-height: 1.2;
  }
  .company-name {
    display: block;
    font-size: 33px;
    font-weight: 400;
  }
  .company-tagline {
    display: block;
    font-size: 29px;
    font-weight: 700;
  }
  .address {
    position: absolute;
    left: 233px;
    top: 194px;
    font-style: normal;
    font-size: 29px;
    font-weight: 300;
    line-height: 36px;
    color: var(--on-blue-soft);
  }
  .website {
    position: absolute;
    left: 233px;
    top: 498px;
    font-size: 29px;
    font-weight: 300;
    color: var(--on-blue-soft);
  }
</style>
</head>
<body>
<main class="card">
  <section class="card-front">
    <div class="brand">
      <span class="brand-dot" aria-hidden="true"></span>
      <span class="brand-name">
        <span class="primary">Meridale</span>
        <span class="secondary">CLEANING SERVICES</span>
      </span>
    </div>

    <div class="person">
      <h1 class="person-name">Colm Varetti</h1>
      <p class="person-role">operations manager</p>
    </div>

    <dl class="contact-list">
      <dt>T</dt><dd>02 9373 6204</dd>
      <dt>F</dt><dd>02 8645 7712</dd>
      <dt>M</dt><dd>04 3857 1490</dd>
    </dl>

    <div class="email">meridaleclean@wexanet.com.au</div>
  </section>

  <section class="card-back">
    <div class="company">
      <span class="company-name">Meridale</span>
      <span class="company-tagline">cleaning services</span>
    </div>
    <address class="address">
      47 Tolly RD Pymble NSW 2073<br>
      PO Box 5832 North Ryde NSW 2113
    </address>
    <div class="website">meridalecleaningservices.com.au</div>
  </section>
</main>
</body>
</html>
```